Marketing Agency Needs Fresh New Look

QuillBeaconWorks.com is a Digital Marketing agency with locations in North Carolina and Florida. And, yes, we do custom Websites too. When we're designing for ourselves, we prefer to outsource because we typically get fresher perspectives from designers involved in the project. Which is why we're here today posting this Redesign project for our very own website.

Overall, we like our website look/feel....but don't LOVE it. We need our new site to be a bit fresher and more current using some of today's web design/development trends.

Some of the details: We want to use more current font styles and sizes (ideally, we use 3 different fonts including one "handwritten" or script font). We use the little nerdy scientist way too much throughout our website. We want to project a positive, friendly image to our customers....but we also want to be considered serious professionals in our industry(s). So, we would like to see a better mix of fun & friendly with professional & completely capable.

Here are two examples of our local competitors and websites that we think are very well done and include some of elements we're looking to see on our new site:

1) www.pixelmongrels.com = these guys do a great job at mixing their cartoony dinosaur with realism imagery. Very clean & professional website, but also cool and interesting how they carry through some of their branding and toony graphic elements. We like the use of big circles to highlight certain elements. We feel that this would play well for us too because we already use some of these big circles/bubbles in our bokeh background.

2) www.vantoloweb.com = these guys have the same kind of top to bottom layout with big chunks for each section. They come across as a little more "buttoned up" then pixelmongrels, but still friendly enough to make a small business owner feel comfortable.

There are a few elements that we consider part of our brand and that we want to continue to use in our new design. They are as follows:
1) The nerdy scientist dude....we have 50+ variations of this little guy in every file format you need. I'll try to upload the whole set....at the least, you'll have one or two examples.

2) The electric green bokeh background you see at the top of each page of our website.

3) And our logo of course which is included in uploads.

Please feel free to ask me any questions. We're really open to new and fresh ideas and creativity. So...let 'r rip!

```html
<!DOCTYPE html>
<html lang="en">
<head>
<meta charset="utf-8">
<title>Quill Beacon Works</title>
<link rel="stylesheet" href="https://fonts.googleapis.com/css2?family=Ubuntu:wght@400;500;700&display=swap">
<style>
:root{
  --green:#6ab536;
  --brand:#7cb82f;
  --lime:#c8e200;
  --yellow:#fdd000;
  --blue:#2aa0d8;
  --ink:#45464c;
  --nav:#b9b9b9;
  --rule:#d6d6d6;
  --client:#8a8a8a;
  --dark:#282828;
  --black:#000;
  --white:#fff;
  --soft:#d8d8d8;
}
*{margin:0;padding:0;box-sizing:border-box}
html,body{width:856px;height:1200px;overflow:hidden;background:var(--white)}
body{font-family:"Ubuntu",sans-serif}
.page{position:relative;width:856px;height:1200px;overflow:hidden}
.abs{position:absolute}

/* header */
.brand{left:151px;top:34px;display:flex;align-items:center;gap:7px}
.brand-dot{width:12px;height:12px;border-radius:50%;background:var(--brand)}
.brand-name{color:var(--brand);font-weight:700;font-size:15px;line-height:16px}
.nav-rule{top:48px;width:1px;height:26px;background:var(--rule)}
.nav-link{top:57px;font-size:9px;font-weight:700;letter-spacing:1.2px;color:var(--nav);transform:translateX(-50%)}
.nav-link.active{color:var(--brand)}

/* banner */
.banner{left:0;top:117px;width:856px;height:66px;
  background:radial-gradient(circle at 10% 30%,rgba(255,255,255,.25) 0 38px,transparent 40px),
  radial-gradient(circle at 77% 40%,rgba(255,255,255,.18) 0 44px,transparent 46px),
  radial-gradient(circle at 92% 10%,rgba(255,255,255,.2) 0 30px,transparent 32px),
  linear-gradient(90deg,#5fa218,#7dc12a 50%,#5fa218)}
.banner-title{left:0;top:117px;width:856px;line-height:66px;text-align:center;color:var(--white);font-size:21px;font-weight:500;letter-spacing:2.4px}

/* clients */
.clients-title{left:0;top:247px;width:856px;text-align:center;font-size:22px;font-weight:700;color:var(--ink)}
.clients-title span{color:var(--yellow)}
.client{transform:translate(-50%,-50%);color:var(--client);font-size:13px;font-weight:700;white-space:nowrap;text-align:center}
.client.boxed{background:#fafafa;padding:28px 18px}

/* social band */
.tile{top:554px;height:104px;display:flex;align-items:center;justify-content:center}
.tile svg{width:62px;height:68px}

/* footer */
.footer{left:0;top:658px;width:856px;height:445px;background:var(--dark)}
.foot-title{font-size:17px;font-weight:700;color:var(--soft);top:713px}
.foot-title .g{color:var(--yellow)}
.foot-title .l{color:var(--lime)}
.contact-icon{left:149px;width:36px;height:36px}
.contact-text{left:197px;color:var(--white);font-size:11.5px;font-weight:700;line-height:19px}
.field-label{left:428px;font-size:10.5px;font-weight:500;color:var(--soft)}
.field-line{left:428px;width:290px;border-top:1.5px dashed var(--soft)}
.send-btn{left:538px;top:1007px;width:180px;height:37px;background:var(--lime);color:#333;font-size:12.5px;font-weight:700;display:flex;align-items:center;justify-content:center;gap:6px}
.bottom{left:0;top:1103px;width:856px;height:97px;background:var(--black)}
.copyright{left:0;top:1144px;width:856px;text-align:center;color:var(--white);font-size:11px;font-weight:700}
.copyright span{color:var(--lime)}
</style>
</head>
<body>
<div class="page">

  <div class="abs brand"><div class="brand-name">Quill Beacon<br>Works</div><div class="brand-dot"></div></div>
  <div class="abs nav-rule" style="left:274px"></div>
  <div class="abs nav-link" style="left:315px">WHO</div>
  <div class="abs nav-rule" style="left:356px"></div>
  <div class="abs nav-link" style="left:396px">WHAT</div>
  <div class="abs nav-rule" style="left:435px"></div>
  <div class="abs nav-link active" style="left:478px">HOW</div>
  <div class="abs nav-rule" style="left:518px"></div>
  <div class="abs nav-link" style="left:560px">WHY</div>
  <div class="abs nav-rule" style="left:601px"></div>
  <div class="abs nav-link" style="left:655px">CONTACT</div>

  <div class="abs banner" role="img" aria-label="Electric green bokeh background"></div>
  <div class="abs banner-title">CREATE MARKETING CHEMISTRY</div>

  <h2 class="abs clients-title">OUR EARS ARE <span>BURNING...</span></h2>
  <div class="abs client" style="left:148px;top:369px">Tailwag Pet Care</div>
  <div class="abs client" style="left:285px;top:360px">Ardent &amp; Moss</div>
  <div class="abs client" style="left:409px;top:367px">Calder Partners</div>
  <div class="abs client" style="left:529px;top:360px">R. Linwood, DDS</div>
  <div class="abs client boxed" style="left:684px;top:368px">Brightsweep</div>
  <div class="abs client" style="left:184px;top:456px">Oakline Floors</div>
  <div class="abs client" style="left:344px;top:452px">Stillwater Wellness</div>
  <div class="abs client" style="left:500px;top:457px">Swift Haul</div>
  <div class="abs client boxed" style="left:659px;top:464px;padding:20px 22px">Terrace Co</div>

  <div class="abs tile" style="left:0;width:205px;background:var(--green)">
    <svg viewBox="0 0 60 66" role="img" aria-label="Search link"><circle cx="33" cy="4" r="3" fill="#fff"/><circle cx="26" cy="11" r="2" fill="#fff"/><path d="M25 16h10v12l17 29q3 7-4 7H12q-7 0-4-7l17-29z" fill="#fff"/><text x="30" y="54" text-anchor="middle" font-family="Ubuntu,sans-serif" font-size="8" font-weight="700" fill="#6ab536">Search</text></svg>
  </div>
  <div class="abs tile" style="left:207px;width:221px;background:var(--lime)">
    <svg viewBox="0 0 60 66" role="img" aria-label="Social link"><circle cx="33" cy="4" r="3" fill="#fff"/><circle cx="26" cy="11" r="2" fill="#fff"/><path d="M25 16h10v12l17 29q3 7-4 7H12q-7 0-4-7l17-29z" fill="#fff"/><text x="30" y="54" text-anchor="middle" font-family="Ubuntu,sans-serif" font-size="8" font-weight="700" fill="#c8e200">Social</text></svg>
  </div>
  <div class="abs tile" style="left:430px;width:212px;background:var(--yellow)">
    <svg viewBox="0 0 60 66" role="img" aria-label="Feed link"><circle cx="33" cy="4" r="3" fill="#fff"/><circle cx="26" cy="11" r="2" fill="#fff"/><path d="M25 16h10v12l17 29q3 7-4 7H12q-7 0-4-7l17-29z" fill="#fff"/><text x="30" y="54" text-anchor="middle" font-family="Ubuntu,sans-serif" font-size="8" font-weight="700" fill="#fdd000">Feed</text></svg>
  </div>
  <div class="abs tile" style="left:644px;width:212px;background:var(--blue)">
    <svg viewBox="0 0 60 66" role="img" aria-label="Posts link"><circle cx="33" cy="4" r="3" fill="#fff"/><circle cx="26" cy="11" r="2" fill="#fff"/><path d="M25 16h10v12l17 29q3 7-4 7H12q-7 0-4-7l17-29z" fill="#fff"/><text x="30" y="54" text-anchor="middle" font-family="Ubuntu,sans-serif" font-size="8" font-weight="700" fill="#2aa0d8">Posts</text></svg>
  </div>

  <div class="abs footer"></div>
  <h3 class="abs foot-title" style="left:149px">GET IN <span class="g">TOUCH</span></h3>
  <h3 class="abs foot-title" style="left:428px">SAY <span class="l">HELLO</span></h3>

  <svg class="abs contact-icon" style="top:770px" viewBox="0 0 36 36" fill="none" stroke="#d8d8d8" stroke-width="2" stroke-linejoin="round"><path d="M2 7l10-4 12 4 10-4v26l-10 4-12-4-10 4z"/><path d="M12 3v26M24 7v26"/></svg>
  <div class="abs contact-text" style="top:767px">410 E. Larkspur Ave. Ste 112<br>Palm Cove, FL 32099</div>

  <svg class="abs contact-icon" style="top:842px" viewBox="0 0 36 36" fill="none" stroke="#d8d8d8" stroke-width="2" stroke-linecap="round"><path d="M10 3l6 7-4 4q3 7 10 10l4-4 7 6-4 6Q14 32 4 9z"/></svg>
  <div class="abs contact-text" style="top:843px">(800) 555-0142<br>(919) 555-0187 &amp; (407) 555-0163</div>

  <svg class="abs contact-icon" style="top:921px" viewBox="0 0 36 36" fill="none" stroke="#d8d8d8" stroke-width="2" stroke-linejoin="round"><rect x="2" y="3" width="32" height="30"/><path d="M2 3l16 17 16-17M2 33l12-13M34 33L22 20"/></svg>
  <div class="abs contact-text" style="top:916px">76 W Corbel St. Ste 300<br>Brookhaven, NC 27655</div>

  <svg class="abs contact-icon" style="top:1003px" viewBox="0 0 36 36" fill="none" stroke="#d8d8d8" stroke-width="2"><rect x="3" y="3" width="30" height="30" stroke-dasharray="3 2"/><rect x="9" y="9" width="18" height="18"/><path d="M12 21l5-5 4 4 3-3"/></svg>
  <div class="abs contact-text" style="top:999px">76 W Corbel St. Ste 300<br>Brookhaven, NC 27655</div>

  <svg class="abs" style="left:430px;top:777px;width:36px;height:37px" viewBox="0 0 36 37" fill="none" stroke="#d8d8d8" stroke-width="2" stroke-linejoin="round"><path d="M34 2L2 18l12 4 4 13 16-33z"/><path d="M14 22L34 2"/></svg>

  <div class="abs field-label" style="top:851px">NAME</div>
  <div class="abs field-line" style="top:866px"></div>
  <div class="abs field-label" style="top:897px">EMAIL</div>
  <div class="abs field-line" style="top:913px"></div>
  <div class="abs field-label" style="top:943px">MESSAGE</div>
  <div class="abs field-line" style="top:959px"></div>
  <div class="abs send-btn">GET IN TOUCH <svg width="6" height="8" viewBox="0 0 6 8"><path d="M0 0l6 4-6 4z" fill="#333"/></svg></div>

  <div class="abs bottom"></div>
  <p class="abs copyright"><span>© Copyright</span> will be added for 2014 &nbsp;after signoff</p>
</div>
</body>
</html>
```